Torvale Works- Plumbing Business Card

We need a business card design for a new company that services Canberra and surrounds. We are a professional family-owned plumbing company who has 20+ years' experience. We would like to use our logo as well as the colours black, white, grey and the signature green. The final design needs to communicate professional, high-end, plumbing with reliable service. We provide obligation free quotes and are open 24/7. Services include: Bathroom/kitchen renovations, drainage, stormwater, water leaks, plumbing maintenance, water tanks and septics.

Target Market(s)

Homeowners, real estate agents, builders, small business owners

Industry/Entity Type

Plumbing & Construction

Font styles to use
Serif
Sans Serif

Colors
59FF00
82FF00
B8FF75
E3FFCB
F4FFEA

Requirements
Must have
• Must have logo, example of services and contact details

```html
<!DOCTYPE html>
<html lang="en">
<head>
<meta charset="utf-8">
<title>Torvale Works – Business Card</title>
<link rel="stylesheet" href="https://fonts.googleapis.com/css2?family=Montserrat:wght@400;700;800&family=Roboto:wght@400;700&display=swap">
<style>
  :root {
    --backdrop: #262626;
    --card: #000000;
    --green: #08a008;
    --white: #ffffff;
  }
  * { margin: 0; padding: 0; box-sizing: border-box; }
  html, body { width: 1200px; height: 757px; overflow: hidden; }
  body { background: var(--backdrop); position: relative; font-family: "Montserrat", sans-serif; }

  .card {
    position: absolute; top: 233px; width: 486px; height: 291px;
    background: var(--card); overflow: hidden;
  }
  .card-front { left: 99px; }
  .card-back { left: 615px; }

  .person-name {
    position: absolute; left: 35px; top: 33px;
    font: 700 21px/1 "Montserrat", sans-serif; color: var(--green); letter-spacing: 0.2px;
  }
  .person-role {
    position: absolute; left: 35px; top: 57px;
    font: 400 12px/1 "Montserrat", sans-serif; color: var(--white);
  }

  .address-icon { position: absolute; left: 35px; top: 154px; width: 15px; height: 15px; }
  .address {
    position: absolute; left: 54px; top: 154px;
    font: 400 11.5px/14px "Montserrat", sans-serif; color: var(--white);
  }

  .contact-bar {
    position: absolute; left: 31.5px; top: 193px; width: 19px; height: 98px;
    background: var(--green); border-radius: 9.5px 9.5px 0 0;
  }
  .contact-icon { position: absolute; left: 34px; width: 14px; height: 14px; }
  .contact-line {
    position: absolute; left: 54px;
    font: 400 11.5px/14px "Montserrat", sans-serif; color: var(--white);
  }
  .phone-icon, .phone { top: 199px; }
  .email-icon, .email { top: 221px; }
  .web-icon, .web { top: 242px; }

  .brand-name {
    position: absolute; font-family: "Montserrat", sans-serif; font-weight: 800;
    color: var(--green); line-height: 0.95; letter-spacing: 0.5px;
  }
  .card-front .brand-name { left: 243px; top: 172px; font-size: 39px; }
  .card-back .brand-name { left: 41px; top: 113px; font-size: 28px; }

  .services-banner {
    position: absolute; left: 223px; top: 58px; width: 263px; height: 32px;
    background: var(--green); border-radius: 16px 0 0 16px;
    font: 700 20px/32px "Roboto", sans-serif; color: var(--white); padding-left: 10px;
    letter-spacing: -0.2px;
  }
  .service-list {
    position: absolute; left: 238px; top: 96px; list-style: none;
    font: 400 15px/23.5px "Roboto", sans-serif; color: var(--white);
  }
  .service-list li { position: relative; padding-left: 10px; }
  .service-list li::before {
    content: ""; position: absolute; left: 0; top: 10px; width: 4px; height: 4px;
    border-radius: 50%; background: var(--green);
  }
</style>
</head>
<body>
  <section class="card card-front">
    <h1 class="person-name">MARA QUINLAN</h1>
    <p class="person-role">CEO/Manger</p>

    <svg class="address-icon" viewBox="0 0 15 15" aria-hidden="true">
      <rect width="15" height="15" rx="2" fill="var(--green)"/>
      <path d="M7.5 2.5a3.3 3.3 0 0 0-3.3 3.3c0 2.5 3.3 6.4 3.3 6.4s3.3-3.9 3.3-6.4a3.3 3.3 0 0 0-3.3-3.3zm0 4.6a1.3 1.3 0 1 1 0-2.6 1.3 1.3 0 0 1 0 2.6z" fill="#fff"/>
    </svg>
    <p class="address">88 Kestrel Row Suite 12<br>Fyshwick, ACT 2609</p>

    <div class="contact-bar"></div>
    <svg class="contact-icon phone-icon" viewBox="0 0 14 14" aria-hidden="true">
      <path d="M3.2 1.5l2 2.4-1 1.4c.8 1.7 2 2.9 3.7 3.7l1.4-1 2.4 2-1 1.8C6.4 11.6 2.4 7.6 2.2 2.5z" fill="#fff"/>
    </svg>
    <p class="contact-line phone">02-6180-4417</p>
    <svg class="contact-icon email-icon" viewBox="0 0 14 14" aria-hidden="true">
      <rect x="1.5" y="3.5" width="11" height="7.5" fill="#fff"/>
      <path d="M1.5 3.5l5.5 4.2 5.5-4.2M1.5 11l4-3.8M12.5 11l-4-3.8" stroke="var(--green)" stroke-width="0.9" fill="none"/>
    </svg>
    <p class="contact-line email">info@torvaleworks.com</p>
    <svg class="contact-icon web-icon" viewBox="0 0 14 14" aria-hidden="true">
      <path d="M4 1.5v10l2.4-2.3 1.7 3.6 1.4-.7-1.7-3.5h3.3z" fill="#fff"/>
    </svg>
    <p class="contact-line web">torvaleworks.com</p>

    <p class="brand-name">TORVALE<br>WORKS</p>
  </section>

  <section class="card card-back">
    <p class="brand-name">TORVALE<br>WORKS</p>
    <h2 class="services-banner">24/7. Services include:</h2>
    <ul class="service-list">
      <li>Bathroom/kitchen renovations</li>
      <li>Drainage</li>
      <li>Stormwater</li>
      <li>Water leaks</li>
      <li>Plumbing maintenance</li>
      <li>Water tanks and septics</li>
    </ul>
  </section>
</body>
</html>
```